Web Design Project

This as the foundation http://lunorbix.com/demo_viewer/index.php?theme=velquistwp

Site needs to have a glossy black background with white text…..Extremely modern with a few flares of ravelle 6 style but nothing too off the wall, easily understood.

Here are some other reference sites and likes and dislikes that will help: (Probably overkill but we are looking for a cutting edge New York / LA Style )

http://www.torvikandcolb.com

Like- The black background with white font is very eye catching and clean. Love the contrast. Black is a great background for photographs and videos

http://samuelvorne.com

Like- Clean homepage, black and white color scheme works well.

http://douglaswhitcanephotography.com

Like- Nice Menu, nice B and W contrast

http://www.qkv.com

Like- Like the Menu. Clean and easy.

http://www.saffelmont.com

Like- Contrast of white background with black font.

Like- Slide show of stills (but should be able to click images to go to video. We’d also like the name of the project)

Like- Drop down menu allows for customer to find service they need without going through all services.

Like- Tells you work that they do right next to the logo.

Dislike- Too much information on homepage. Too much scrolling.

http://www.corbelvanestudios.com

Like- High Res images on home page

Like - The About Me is on homepage and speaks to potential customer directly. “We create award-winning videos for companies like yours.”

Like- Blog is updated with new projects they do. And short, visual entries

Like- “Work” section stands out from website. The background fades to light grey and white when you click on “work” so that the portfolio stands out more. Makes color look more vivid

Like- Black and white color scheme with grey header

http://www.fennwick748.com

Like- High Res images on home page pointing to projects

Like- Photograph as background, changes with different links. So work is always showcased and creates contrast. Information is laid over a barely translucent background, which is laid over the picture.

Like- They have a good Attitude about quality of their product

http://www.quillbramt.net

Like- First thing you see when open page is a clear big statement about what they do, said in a catchy way. They have a Tagline.

http://plimsworthdesign.com

Like- How work is categorized. Client list has links, which take you to their Client page with all their work grouped together. Nice flow and organization shows client relationships. And nice descriptions of what the job was and how it was executed… Way too wordy at times though

http://www.marivantphotography.com

Like- The homepage is very clean and accessible. Love the color scheme and how Logo is centered between the links.

Of the four designs we have gotten EVERY SINGLE ONE has been a template STOLEN from another site. We are paying for ORIGINAL design. Not copies and templates. Please ONLY submit original designs

```html
<!DOCTYPE html>
<html lang="en">
<head>
<meta charset="utf-8">
<title>Vexmoor Productions</title>
<link href="https://fonts.googleapis.com/css2?family=Yanone+Kaffeesatz:wght@300;400;600&family=Titillium+Web:ital,wght@1,700;1,900&family=Quicksand:wght@300&display=swap" rel="stylesheet">
<style>
:root{
  --black:#000;
  --white:#fff;
  --frame:#2b2b2b;
  --muted:#d6d6d6;
  --field:#ececec;
  --field-line:#555;
  --social:#8a8a8a;
}
*{box-sizing:border-box;margin:0;padding:0}
html,body{width:834px;height:1200px;overflow:hidden;background:var(--black)}
body{position:relative;font-family:"Yanone Kaffeesatz",sans-serif;color:var(--white)}
.abs{position:absolute}

.main-nav{position:absolute;top:0;left:0;width:834px;height:44px;display:flex;justify-content:space-between;padding:8px 38px 0 45px;z-index:3}
.main-nav a{color:var(--white);text-decoration:none;font-size:19px;font-weight:300;letter-spacing:-.2px}

.stage{position:absolute;top:0;left:0;width:834px;height:560px}
.brand{top:122px;left:0;width:834px;text-align:center;font-family:"Yanone Kaffeesatz",sans-serif;font-size:13px;letter-spacing:3px;color:var(--white);font-weight:400}

.thumb{position:absolute;width:139px;height:97px;border:5px solid var(--frame);border-radius:14px;overflow:hidden}
.thumb div{width:100%;height:100%}
.t1 div{background:linear-gradient(135deg,#4a3a30,#b49a80 50%,#2a2220)}
.t2 div{background:linear-gradient(135deg,#c04070,#e0c040 35%,#3080c0 70%,#402030)}
.t3 div{background:linear-gradient(180deg,#6a7a90,#d0b040 60%,#505050)}
.t4 div{background:linear-gradient(135deg,#1a1a1a,#d8d0c8 55%,#3a3030)}
.t5 div{background:linear-gradient(180deg,#f0f0f0,#d0d8a0 50%,#6a9a30)}
.t6 div{background:linear-gradient(135deg,#000,#102040 40%,#e040a0 65%,#20c0d0 85%)}

.headline{top:190px;left:0;width:834px;text-align:center;color:var(--black);line-height:1}
.headline .strong{display:block;font-family:"Titillium Web",sans-serif;font-style:italic;font-weight:900;font-size:31px;letter-spacing:-.5px}
.headline .light{display:block;font-family:"Quicksand",sans-serif;font-weight:300;font-size:36px;margin-top:4px;letter-spacing:-1px}

.player{left:243px;top:271px;width:357px;height:189px;border:6px solid var(--black);border-radius:20px;overflow:hidden}
.player .screen{width:100%;height:100%;background:linear-gradient(100deg,#f4f8fa 0%,#cfe6f2 35%,#7fc0e0 60%,#e9f3f8 100%)}
.player svg{position:absolute;right:14px;bottom:14px}

.studio{top:498px;left:0;width:834px;text-align:center}
.studio strong{display:block;font-size:15px;font-weight:600}
.studio span{display:block;font-size:12px;font-weight:300;margin-top:1px}

h2{font-weight:300;line-height:1}
.about-title{left:25px;top:612px;font-size:30px}
.exp-title{left:551px;top:612px;font-size:30px}
.copy{font-size:11.5px;line-height:14.4px;font-weight:300}
.about-copy{left:25px;top:655px;width:360px}
.exp-copy{left:551px;top:655px;width:270px}
.more{font-size:13px;font-weight:400;color:var(--white);text-decoration:none}
.about-more{left:26px;top:721px}
.exp-more{left:551px;top:778px}

.services-lead{left:20px;top:797px;font-size:18.5px;font-weight:300;line-height:19px;width:360px}
.service-list{list-style:none;font-size:13px;font-weight:300;line-height:16.5px;color:var(--muted)}
.col-a{left:21px;top:851px;width:170px}
.col-b{left:196px;top:851px;width:180px}

.quote-label{right:15px;top:828px;font-size:12.5px;font-weight:400}
.quote-form{left:552px;top:848px;width:274px;height:217px;background:var(--white);border-radius:10px;color:var(--black)}
.field{position:absolute;left:16px;font-size:11.5px}
.field label{position:absolute;left:0;top:2px;white-space:nowrap}
.field .input{position:absolute;left:52px;width:187px;height:19px;background:var(--field);border:1px solid var(--field-line)}
.f1{top:17px}.f2{top:47px}.f3{top:76px}.f4{top:107px}
.f4 .input{height:70px}
.submit{position:absolute;left:69px;top:187px;width:63px;height:24px;background:var(--black);color:var(--white);font-family:"Yanone Kaffeesatz",sans-serif;font-size:12px;border:0;border-radius:2px}

.copyright{left:21px;top:1170px;font-size:12px;font-weight:300;color:#bbb}
.share{left:724px;top:1166px;font-size:16px;font-weight:400;letter-spacing:-.5px}
.social{position:absolute;top:1161px;width:24px;height:24px;border-radius:50%;background:var(--social)}
.s1{left:759px}.s2{left:788px}
</style>
</head>
<body>
<nav class="main-nav">
  <a href="#">HOME</a><a href="#">ABOUT US</a><a href="#">REELS</a><a href="#">VIDEO GALLERY</a><a href="#">PHOTO GALLERY</a><a href="#">VIDEO BLOG</a><a href="#">CLIENTS</a><a href="#">FAQ</a><a href="#">CONACT US</a>
</nav>

<svg class="stage" width="834" height="560" viewBox="0 0 834 560" aria-hidden="true">
  <rect width="834" height="560" fill="#fff"/>
  <path d="M0 0H834V48C690 40 560 80 490 125 450 150 380 160 330 140 250 110 180 75 0 98Z" fill="#000"/>
  <path d="M0 104C180 82 250 118 330 148 380 166 452 158 494 131 565 86 690 46 834 56" fill="none" stroke="#000" stroke-width="2"/>
  <path d="M0 553C150 553 220 530 300 504 360 486 470 482 540 498 640 520 700 553 834 553V560H0Z" fill="#000"/>
</svg>

<div class="abs brand">Vexmoor Productions</div>

<div class="thumb t1" style="left:30px;top:106px"><div role="img" aria-label="Band photo shoot still"></div></div>
<div class="thumb t2" style="left:30px;top:251px"><div role="img" aria-label="Crowd at a colorful party event"></div></div>
<div class="thumb t3" style="left:30px;top:403px"><div role="img" aria-label="City street with a yellow taxi"></div></div>
<div class="thumb t4" style="left:668px;top:106px"><div role="img" aria-label="Wedding couple portrait"></div></div>
<div class="thumb t5" style="left:668px;top:251px"><div role="img" aria-label="Dancers in costume on stage"></div></div>
<div class="thumb t6" style="left:668px;top:403px"><div role="img" aria-label="Phone product promo with colored tiles"></div></div>

<div class="abs headline">
  <span class="strong">FULL SERVICE HD</span>
  <span class="light">VIDEO PRODUCTION</span>
</div>

<div class="abs player">
  <div class="screen" role="img" aria-label="Hotel campaign video: hand touching pool water"></div>
  <svg width="36" height="36" viewBox="0 0 36 36" aria-hidden="true">
    <circle cx="18" cy="18" r="16" fill="none" stroke="#fff" stroke-width="2"/>
    <path d="M14 10L26 18 14 26Z" fill="#fff"/>
  </svg>
</div>

<div class="abs studio">
  <strong>Vexmoor Productions</strong>
  <span>48 W.31st Street, Suite 410, New York, NY 10001 212-555-0147</span>
</div>

<h2 class="abs about-title">ABOUT US</h2>
<p class="abs copy about-copy">&nbsp;Our New York City-based video production company offers a full &nbsp;top full service video studio and work in a wide range of media and styles. For over 30 years we have specialized in all aspects of video production from commercials and training video to legal video and video for non-profit organizations.</p>
<a class="abs more about-more" href="#">MORE</a>

<h2 class="abs exp-title">Over 30 Years Of Experience</h2>
<p class="abs copy exp-copy">&nbsp;Our New York City-based video production company offers a full range of video production services, from storyboarding and scriptwriting to videotaping, post production editing and graphic design. We are a one-stop full service video studio and work in a wide range of media and styles. For over 30 years we have specialized in all aspects of video production from commercials and training video to legal video and video for non-profit organizations.</p>
<a class="abs more exp-more" href="#">MORE</a>

<p class="abs services-lead">High definition video, location, and studio shoots, post production with award winning editors.</p>
<ul class="abs service-list col-a">
  <li>Crowd-sourcing and Promotional Commercials</li>
  <li>Promotional Videos</li>
  <li>Corporate Videos</li>
  <li>Documentaries</li>
</ul>
<ul class="abs service-list col-b">
  <li>Event Video and Photography</li>
  <li>Oral Histories</li>
  <li>Training Videos</li>
  <li>Webcasting</li>
  <li>Multilingual Video Translation</li>
  <li>Music Videos</li>
</ul>

<p class="abs quote-label">Contact Us For A Free Quote</p>
<form class="abs quote-form">
  <div class="field f1"><label>name :</label><span class="input"></span></div>
  <div class="field f2"><label>email :</label><span class="input"></span></div>
  <div class="field f3"><label>website :</label><span class="input"></span></div>
  <div class="field f4"><label>message :</label><span class="input"></span></div>
  <button class="submit" type="button">submit</button>
</form>

<p class="abs copyright">©2013 Vexmoor Productions All Rights Reserved.</p>
<span class="abs share">SHARE</span>
<a class="social s1" href="#" aria-label="Share link one"></a>
<a class="social s2" href="#" aria-label="Share link two"></a>
</body>
</html>
```